School Auction Party Invitation- Create... the Future.

We need a logo design and invitation for our school auction fundraiser party. Our theme is Create.... The Future. We are trying to incorporate technology, creativity, 21st century learning, and make use of fun, graphic design. colors: black, white, silver, and a bright(almost neon) accent colors. (orange-primary)
Updates

Deadline update: Logo-October 23, Invite- Nov. 7

Target Market(s)

Parents of a private preschool-8th grade students from the Bay Area (majority age 40s, some 30s and 50s) All passionate about kids, education, some varying backgrounds/incomes, but majority upper class-educated. annual school auction/fundraiser. want to create interest/excitement- fun community party. we are trying to focus the theme on creativity & the future (technology, our kid's futures, etc)
www.morvendale.org

Industry/Entity Type

School

Requirements
Must have
• Logo file, One page invite (5x7 including date, time, place, rsvp info, need digital file to print locally

add band logo (possibly tie in to invite look) www.quietharborkitesband.com
Nice to have
• fun, creative, futuristic, abstract, sleek, graphic art. we will be using LED & glow lights at fundraiser
Should not have
• pictures of people

```html
<!DOCTYPE html>
<html lang="en">
<head>
<meta charset="utf-8">
<title>Create the Future – Annual Auction Gala Invitation</title>
<link rel="stylesheet" href="https://fonts.googleapis.com/css2?family=Arvo:ital,wght@0,400;0,700;1,400&family=Bowlby+One+SC&family=Monoton&family=Oswald:wght@600&family=Questrial&display=swap">
<style>
  :root {
    --orange: #f26a2e;
    --grey: #8d8f92;
    --silver: #b9bbbe;
    --ink: #1b1b1b;
    --navy: #2f3a55;
    --paper: #ffffff;
    --rule: #d6d6d6;
  }
  * { margin: 0; padding: 0; box-sizing: border-box; }
  html, body { width: 857px; height: 1200px; overflow: hidden; background: var(--paper); }
  .invite {
    position: relative; width: 857px; height: 1200px;
    background: var(--paper); border: 2px solid var(--rule);
    color: var(--ink); font-family: "Arvo", serif;
  }
  .invite > * { position: absolute; }

  .theme-mark {
    left: 40px; top: 50px; width: 180px; height: 180px;
    border-radius: 50%; background: var(--orange);
  }
  .theme-name {
    left: 260px; top: 56px;
    font-family: "Arvo", serif; font-weight: 700;
    font-size: 76px; line-height: 1.2; color: var(--orange);
  }

  .gala-title {
    left: 0; width: 100%; top: 336px; text-align: center;
    font-weight: 700; font-size: 28px; color: var(--navy);
  }
  .gala-intro {
    left: 0; width: 100%; top: 378px; text-align: center;
    font-size: 25px; line-height: 1.15;
  }

  .date-day { left: 62px; top: 478px; font-family: "Bowlby One SC", sans-serif; font-size: 36px; line-height: 1; }
  .date-num { left: 66px; top: 520px; font-family: "Monoton", sans-serif; font-size: 80px; color: var(--orange); line-height: 1; }
  .date-month { left: 62px; top: 620px; font-family: "Bowlby One SC", sans-serif; font-size: 34px; line-height: 1; }
  .date-year {
    left: 322px; top: 650px; transform: rotate(-90deg); transform-origin: left top;
    font-family: "Questrial", sans-serif; font-size: 30px; letter-spacing: 0.3em; line-height: 1;
  }

  .venue { left: 420px; top: 486px; font-family: "Questrial", sans-serif; font-style: normal; font-size: 30px; line-height: 1.05; }
  .venue-name { color: var(--orange); }
  .venue-address { margin-top: 6px; color: var(--ink); }

  .schedule { left: 131px; top: 720px; width: 700px; }
  .slot { margin-bottom: 12px; }
  .slot-time { font-weight: 700; font-size: 34px; line-height: 1.05; }
  .slot-time small { font-size: 26px; }
  .slot-desc { font-size: 25px; line-height: 1.15; }
  .slot--silent .slot-time { color: var(--silver); }
  .slot--dinner .slot-time { color: var(--ink); }
  .slot--music .slot-time { color: var(--orange); }

  .band { display: flex; align-items: center; gap: 8px; margin-top: 4px; }
  .band svg { width: 70px; height: 20px; }
  .band-name { font-weight: 700; font-size: 22px; letter-spacing: 0.04em; color: var(--orange); }
  .band-note { margin-top: 4px; font-size: 23px; white-space: nowrap; }

  .rsvp {
    left: 0; width: 100%; top: 1072px; text-align: center;
    font-family: "Oswald", sans-serif; font-weight: 600; font-size: 21px; color: var(--navy);
  }
  .tagline {
    left: 0; width: 100%; top: 1150px; text-align: center;
    font-style: italic; font-size: 22px; color: var(--orange); white-space: nowrap;
  }
</style>
</head>
<body>
<main class="invite">
  <div class="theme-mark" aria-hidden="true"></div>
  <div class="theme-name">create<br>the future</div>

  <h1 class="gala-title">The Morvendale School Annual Auction Gala</h1>
  <p class="gala-intro">a celebration to benefit our children’s bright futures<br>and to support our amazing faculty and staff.</p>

  <div class="date-day">SATURDAY THE</div>
  <div class="date-num">22ND</div>
  <div class="date-month">OF MARCH</div>
  <div class="date-year">2014</div>

  <address class="venue">
    <div class="venue-name">LARKSPUR HILLS<br>CLUB</div>
    <div class="venue-address">2250 FERNWOOD<br>LANE ALDERBROOK, CA<br>94601</div>
  </address>

  <section class="schedule">
    <div class="slot slot--silent">
      <div class="slot-time">5:30 <small>p.m.</small></div>
      <div class="slot-desc">Silent Auction, cocktails, and live social time</div>
    </div>
    <div class="slot slot--dinner">
      <div class="slot-time">7:00 <small>p.m.</small></div>
      <div class="slot-desc">Dinner and Live Auction</div>
    </div>
    <div class="slot slot--music">
      <div class="slot-time">8:00 <small>p.m.</small></div>
      <div class="slot-desc">Live music and dancing</div>
      <div class="band">
        <svg viewBox="0 0 70 20" aria-hidden="true">
          <line x1="0" y1="10" x2="58" y2="10" stroke="#8d8f92" stroke-width="4"/>
          <polygon points="52,2 68,10 52,18" fill="#8d8f92"/>
        </svg>
        <span class="band-name">QUIET HARBOR KITES</span>
      </div>
      <div class="band-note">(Bay area band, and Morvendale parent Dan Whitcomb)</div>
    </div>
  </section>

  <p class="rsvp">PLEASE RETURN THE ENCLOSED RSVP CARD OR RSVP ONLINE BY MARCH 14</p>
  <p class="tagline">Take an exciting trip into the future and celebrate our community!</p>
</main>
</body>
</html>
```